HOLTMARK Construction Services
Project: Stationary
Stationary
Simple
Derek Pannell
derek@hltservices-example.com
www.hltservices-example.com
Finalized Draft of the logo can be seen on the following URL: http://www.quillora-example.com/contests/business-logo-264. AI file will be uploaded soon. At the front of the business card the following text should be added design.engineer.build commercial.residential

```html
<!DOCTYPE html>
<html lang="en">
<head>
<meta charset="utf-8">
<title>HOLTMARK Construction Services – Business Cards</title>
<link href="https://fonts.googleapis.com/css2?family=Montserrat:wght@400;600;700&family=Open+Sans:wght@400;600&display=swap" rel="stylesheet">
<style>
  :root {
    --bg: #ffffff;
    --lime: #8cc63f;
    --lime-dark: #79b02f;
    --ink: #2e2e2e;
    --grey-text: #555555;
    --card-light: #f4f4f4;
    --card-dark: #0c0c0c;
    --steel-top: #9a9a9a;
    --steel-mid: #6c6c6c;
    --steel-bottom: #4a4a4a;
    --white: #ffffff;
  }
  * { margin: 0; padding: 0; box-sizing: border-box; }
  html, body { width: 1200px; height: 871px; overflow: hidden; background: var(--bg); }
  .canvas { position: relative; width: 1200px; height: 871px; font-family: "Open Sans", Arial, sans-serif; }

  .card { position: absolute; overflow: hidden; box-shadow: 4px 6px 14px rgba(0,0,0,0.28); }

  /* front card */
  .card--front { left: 30px; top: 30px; width: 720px; height: 365px;
    background: linear-gradient(135deg, #fafafa 0%, var(--card-light) 60%, #e6e6e6 100%); }
  .card--front .holder { position: absolute; left: 40px; top: 75px; font-family: "Montserrat", Arial, sans-serif;
    font-size: 25px; color: var(--ink); letter-spacing: 0.5px; }
  .holder .first { font-weight: 700; }
  .holder .last { font-weight: 400; }
  .card--front .brand { position: absolute; right: 70px; top: 60px; text-align: center; }
  .brand .mark { display: block; margin: 0 auto 10px; width: 58px; height: 58px; border-radius: 50%; background: var(--lime); }
  .brand .name { font-family: "Montserrat", Arial, sans-serif; font-weight: 700; font-size: 34px; letter-spacing: 1px; line-height: 1; }
  .brand .sub { display: block; font-size: 10px; letter-spacing: 2.2px; text-transform: uppercase; margin-top: 4px; color: var(--lime-dark); }
  .card--front .brand .name { color: #555; }

  .contact { position: absolute; left: 40px; top: 224px; font-size: 14px; color: var(--grey-text); line-height: 22px; }
  .contact .label { display: inline-block; width: 68px; font-weight: 600; color: var(--ink); }

  .card--front .band { position: absolute; left: 0; bottom: 0; width: 100%; height: 78px;
    background: linear-gradient(180deg, #9bd14a 0%, var(--lime) 100%); }
  .card--front .band .tagline { position: absolute; left: 40px; top: 28px; font-size: 16px; letter-spacing: 2.4px; color: var(--white); }

  /* back card */
  .card--back { left: 512px; top: 500px; width: 650px; height: 337px; background: var(--card-dark); }
  .card--back .brand { position: absolute; left: 28px; top: 42px; text-align: left; }
  .card--back .brand .mark { margin: 0 0 10px 48px; }
  .card--back .brand .name { color: var(--white); }
  .card--back .brand .web { display: block; font-size: 13px; color: var(--white); margin-top: 6px; }
  .card--back .holder { position: absolute; right: 50px; top: 78px; font-family: "Montserrat", Arial, sans-serif;
    font-size: 23px; color: var(--white); }
  .card--back .contact { left: auto; right: 50px; top: 230px; text-align: right; font-size: 13px; color: var(--white); line-height: 20px; }
  .card--back .contact .email { color: var(--lime); }
  .card--back .contact .label { width: auto; margin-right: 14px; color: var(--white); font-weight: 400; }
  .card--back .band { position: absolute; left: 0; bottom: 0; width: 100%; height: 64px;
    background: linear-gradient(180deg, var(--steel-top) 0%, var(--steel-mid) 55%, var(--steel-bottom) 100%); }
  .card--back .band .tagline { position: absolute; left: 0; right: 0; top: 22px; text-align: center;
    font-family: "Montserrat", Arial, sans-serif; font-weight: 600; font-size: 15px; letter-spacing: 3px; color: var(--lime); }
</style>
</head>
<body>
<main class="canvas">
  <section class="card card--front" aria-label="Business card front">
    <p class="holder"><span class="first">DEREK</span> <span class="last">PANNELL</span></p>
    <div class="brand">
      <span class="mark"></span>
      <span class="name">HOLTMARK</span>
      <span class="sub">Construction Services</span>
    </div>
    <div class="contact">
      <p><span class="label">Phone</span>: 281-555-0147</p>
      <p><span class="label">Email</span>: derek@hltservices-example.com</p>
      <p><span class="label">Website</span>: www.hltservices-example.com</p>
    </div>
    <div class="band"><p class="tagline">Design :: Engineer :: Build Commercial :: Residential</p></div>
  </section>

  <section class="card card--back" aria-label="Business card back">
    <div class="brand">
      <span class="mark"></span>
      <span class="name">HOLTMARK</span>
      <span class="sub">Construction Services</span>
      <span class="web">www.hltservices-example.com</span>
    </div>
    <p class="holder"><span class="first">DEREK</span> <span class="last">PANNELL</span></p>
    <div class="contact">
      <p class="email">derek@hltservices-example.com</p>
      <p><span class="label">Phone</span>281-555-0147</p>
    </div>
    <div class="band"><p class="tagline">RESIDENTIAL :: COMMERCIAL :: REMODEL</p></div>
  </section>
</main>
</body>
</html>
```